Design a label for a dog shampoo names furbloom, the sell point of this series of shampoo is “just like wash your dogs with milk, not harm for your hand ”, the style could be gentle or professional or even amazing.

Use only 2 colors in the design job, the color of our logo could be changed, it depends on your whole page. Please design in CDR or ai.

update:
Pls do more change with the fonts when you design the front page, including title and details. Try more styles of fonts. Addition, this design will be printed on the bottle, no a label stick on it.
Updates

Do not put a real dog or animal on the page, Pay more attention to the types of fonts

Reason: Expect for more design idea.

Target Market(s)

people 20-30 years old who have dogs and cats at home

Industry/Entity Type

It Professional

Requirements
Nice to have
• It would be nice if you add some detail words in the design of the right side.

```html
<!DOCTYPE html>
<html lang="en">
<head>
<meta charset="utf-8">
<title>furbloom Super-Conditioning &amp; Nutrient Shampoo – Label</title>
<link href="https://fonts.googleapis.com/css2?family=Open+Sans:ital,wght@0,400;0,700;1,700;1,800&family=Source+Sans+3:wght@400;700&display=swap" rel="stylesheet">
<style>
  :root{
    --orange:#f7941d;
    --orange-light:#fbb040;
    --blue:#29abe2;
    --white:#ffffff;
    --ink:#111111;
    --gap:#000000;
  }
  *{margin:0;padding:0;box-sizing:border-box}
  html,body{width:1200px;height:1000px;overflow:hidden;background:var(--gap)}
  .label{position:relative;width:1200px;height:1000px}

  /* Front panel */
  .front{position:absolute;left:0;top:0;width:518px;height:1000px;background:var(--white);overflow:hidden;font-family:"Source Sans 3",sans-serif}
  .front__band{position:absolute;left:0;top:0;width:100%;height:115px;background:linear-gradient(180deg,var(--orange-light),var(--orange))}
  .brand{position:absolute;left:0;right:0;top:60px;display:flex;align-items:center;justify-content:center;gap:12px;height:100px}
  .brand__dot{width:22px;height:22px;border-radius:50%;background:var(--blue)}
  .brand__name{font-family:"Source Sans 3",sans-serif;font-weight:700;font-size:46px;color:var(--blue);background:var(--white);padding:4px 18px;border-radius:40px}
  .front__kicker{position:absolute;left:0;right:0;top:246px;text-align:center;color:var(--blue);font-size:27px;letter-spacing:.3px}
  .front__title{position:absolute;left:0;right:0;top:270px;text-align:center;color:var(--blue);font-family:"Open Sans",sans-serif;font-weight:800;font-style:italic;font-size:104px;letter-spacing:-2px;line-height:1.1}
  .front__claim{position:absolute;left:0;right:0;top:393px;text-align:center;color:var(--orange);font-size:22px;line-height:27px}
  .front__claim strong{font-weight:700;font-style:italic}
  .front__photo{position:absolute;left:30px;top:470px;width:260px;height:420px;border-radius:40% 40% 10% 10%;background:radial-gradient(ellipse at 50% 40%,#f1d7a8,#e3bf86 55%,rgba(255,255,255,0) 75%)}
  .front__benefits{position:absolute;left:190px;width:310px;top:542px;text-align:center;color:var(--blue);font-size:34px;line-height:47px}
  .front__curl{position:absolute;left:0;top:0}
  .front__skin{position:absolute;left:305px;top:885px;color:var(--white);font-family:"Open Sans",sans-serif;font-size:30px;transform:rotate(-30deg);transform-origin:left bottom}
  .front__hand{position:absolute;left:420px;top:905px;width:58px;height:70px;border-radius:30px 30px 12px 12px;background:linear-gradient(180deg,#ffffff,#f3f3f3)}
  .front__volume{position:absolute;left:38px;top:955px;color:var(--blue);font-family:"Open Sans",sans-serif;font-weight:700;font-style:italic;font-size:24px}

  /* Back panel */
  .back{position:absolute;left:678px;top:0;width:522px;height:1000px;background:var(--white);overflow:hidden}
  .back__band-top{position:absolute;left:0;top:0;width:100%;height:50px;background:linear-gradient(180deg,var(--orange),var(--orange-light))}
  .back__band-bottom{position:absolute;left:0;bottom:0;width:100%;height:37px;background:var(--orange)}
  .back__copy{position:absolute;left:36px;top:53px;width:451px;color:var(--ink);font-family:"Source Sans 3",sans-serif;font-size:19px;line-height:25.8px}
  .back__copy p{text-align:justify}
  .back__copy h2{font-size:19px;font-weight:700;line-height:25.8px}
  .back__product{font-weight:700}
  .back__product small{font-size:15px;text-transform:uppercase}
  .back__brand{position:absolute;left:0;right:0;bottom:10px;display:flex;justify-content:center;align-items:center;gap:8px}
  .back__brand .brand__dot{width:14px;height:14px}
  .back__brand .brand__name{font-size:28px;padding:2px 12px}
</style>
</head>
<body>
<main class="label">
  <section class="front">
    <div class="front__band"></div>
    <div class="brand"><span class="brand__name">furbloom</span><span class="brand__dot"></span></div>
    <p class="front__kicker">SUPER-CONDITIONING &amp; NUTRIENT</p>
    <h1 class="front__title">SHAMPOO</h1>
    <p class="front__claim">wash your dogs just like with milk<br><strong>not harm</strong> for your hand</p>
    <div class="front__photo" role="img" aria-label="Photo of a golden retriever sitting and smiling"></div>
    <p class="front__benefits">MOISTURE-RICH<br>SMOOTH AND<br>SILKY</p>
    <svg class="front__curl" width="518" height="1000" viewBox="0 0 518 1000" aria-hidden="true">
      <path d="M250 1000 C360 930 460 860 518 740 L518 1000 Z" fill="var(--orange)"/>
      <path d="M518 740 C505 800 470 840 430 860 C470 830 500 790 518 740 Z" fill="var(--orange-light)"/>
    </svg>
    <div class="front__hand" role="img" aria-label="Drawing of an open hand"></div>
    <p class="front__skin">Skin friendly</p>
    <p class="front__volume">1000 ML</p>
  </section>

  <section class="back">
    <div class="back__band-top"></div>
    <div class="back__copy">
      <p><span class="back__product"><small>furbloom</small> Super-Conditioning&amp;Nutrient Shampoo</span> is a specially formulated shampoo, rich in conditioners picked up from milk which subdivide and balance nutrition of pet’s coat. More easier and better assimilate for coat from base to the end after using. With the help of minus-ion, the balancer of nutrition, rinses out quickly and completely to leave a soft, sparkling, and smooth coat. Safe and gentle enough to be used every day. Safe for even the most sensitive skin and coat, puppies, lactating bitches and cats.</p>
      <h2>DIRECTIONS:</h2>
      <p>- Before shampooing, blush out pet’s coat.</p>
      <p>- Saturate dog’s coat with lukewarm water.</p>
      <p>- Dispense a small amount of shampoo into the palm of your hand.</p>
      <p>- To clean coat, start at dog’s head and work back - towards the tail. Avoid getting shampoo into the dog’s eyes and ears.</p>
      <p>- Rinse coat sereral times with lukewarm water.</p>
      <p>- Towel dry and gently comb or brush coat.</p>
      <h2>ACTIVE INGREDIENTS:</h2>
      <p>Hypochlorous Acid, Sodium Hypochlorite</p>
      <h2>USE PRECAUTIONS:</h2>
      <p>Harmful if swallowed. Do not inhale. Discontinue use if irritation develops and contact your veterinarian. For animal use only. Not for human use. Keep out of reach of children. Do not decant into smaller containers. Not for injection. Always consult with a Veterinarian for systemic conditions.</p>
      <h2>STORAGE AND DISPOSAL</h2>
      <p>Keep out of the tough of children. Replace Cap. Wrap in several layers of newspaper and discard in trash.</p>
    </div>
    <div class="back__band-bottom"></div>
    <div class="back__brand"><span class="brand__name">furbloom</span><span class="brand__dot"></span></div>
  </section>
</main>
</body>
</html>
```